B.P.L.H. Letterhead design

I would like a really professionally designed letterhead for my professional tutoring business called "The Bright Pathway Learning House" (B.P.L.H.).Something fresh,modern and inspiring that will breath new life into the bu.The business/centre offers professional tutoring for 6 - 16 year olds in maths and english.

I have also attached a centre picture our logo, our proposed school bag,and our latest newsletter to give some perspective & background.

We like to see designs that use the blue & yellow colour theme.The final design should communicate ... "Giving Your Child A Secure Future ... And You Yourself ... Peace Of Mind!!!"

```html
<!DOCTYPE html>
<html lang="en">
<head>
<meta charset="utf-8">
<title>B.P.L.H. Letterhead</title>
<link rel="stylesheet" href="https://fonts.googleapis.com/css2?family=Alegreya+Sans:wght@400;500&family=Encode+Sans+Condensed:wght@400&display=swap">
<style>
  :root {
    --navy: #2e3a6c;
    --navy-deep: #262f63;
    --sun: #fde46a;
    --paper: #ffffff;
    --contact-ink: #2a2a2a;
    --ghost: #e6e6e6;
    --backdrop: #8a8a8a;
  }
  * { margin: 0; padding: 0; box-sizing: border-box; }
  html, body {
    width: 1200px; height: 1000px; overflow: hidden;
    background: var(--backdrop);
  }
  .letterhead {
    position: absolute; left: 270px; top: 33px;
    width: 660px; height: 934px;
    background: var(--paper);
    box-shadow: 0 2px 6px rgba(0,0,0,.25);
    overflow: hidden;
  }
  .header-band, .footer-band { position: absolute; left: 0; display: block; }
  .header-band { top: 0; }
  .footer-band { bottom: 0; }
  .brand {
    position: absolute; left: 42px; top: 62px;
    font-family: "Alegreya Sans", sans-serif;
    color: var(--sun);
    display: flex; flex-direction: column; align-items: center;
  }
  .brand-row { display: flex; align-items: center; gap: 6px; }
  .brand-mark { width: 10px; height: 10px; background: var(--sun); }
  .brand-name { font-size: 13.5px; font-weight: 500; line-height: 1.1; }
  .brand-rule { width: 100%; height: 1px; background: var(--sun); margin: 3px 0 3px; }
  .brand-tagline { font-size: 8.5px; font-weight: 400; line-height: 1; }
  .contact {
    position: absolute; left: 486px; top: 31px;
    list-style: none;
    font-family: "Encode Sans Condensed", sans-serif;
    font-weight: 400; font-size: 9.5px; color: var(--contact-ink);
  }
  .contact li { display: flex; align-items: center; gap: 6px; height: 14px; white-space: nowrap; }
  .contact svg { width: 9px; height: 9px; flex: none; }
  .ghost-name {
    position: absolute; right: 20px; bottom: 36px;
    font-family: "Alegreya Sans", sans-serif; font-weight: 500;
    font-size: 74px; color: var(--ghost); letter-spacing: 2px;
  }
</style>
</head>
<body>
<main class="letterhead">
  <svg class="header-band" width="660" height="108" viewBox="0 0 660 108" aria-hidden="true">
    <rect width="660" height="108" fill="var(--navy)"/>
    <path d="M300 0 C370 10 400 40 430 70 C460 100 500 106 540 108 L660 108 L660 0 Z" fill="var(--sun)"/>
  </svg>

  <div class="brand">
    <div class="brand-row">
      <span class="brand-mark"></span>
      <span class="brand-name">TheBrightPathwayLearningHouse.co.uk</span>
    </div>
    <span class="brand-rule"></span>
    <span class="brand-tagline">Bright Minds, Secure Futures</span>
  </div>

  <ul class="contact">
    <li><svg viewBox="0 0 10 10"><rect width="10" height="10" rx="1" fill="var(--navy)"/><path d="M3 2h2v1.5H4v3h1V8H3z" fill="#fff"/></svg>+00-7-41580326</li>
    <li><svg viewBox="0 0 10 10"><rect width="10" height="10" rx="1" fill="var(--navy)"/><rect x="2" y="3" width="6" height="4" fill="#fff"/></svg>+00-7-41580327</li>
    <li><svg viewBox="0 0 10 10"><rect width="10" height="10" rx="1" fill="var(--navy)"/><path d="M2 3h6v4H2z M2 3l3 2 3-2" fill="none" stroke="#fff" stroke-width=".8"/></svg>hello@brightpathway.co.uk</li>
    <li><svg viewBox="0 0 10 10"><rect width="10" height="10" rx="1" fill="var(--navy)"/><path d="M5 8.5 3 5a2 2 0 1 1 4 0z" fill="#fff"/></svg>12 Meadow Lane, London, UK, 4417</li>
  </ul>

  <div class="ghost-name" role="img" aria-label="Faint B.P.L.H. name decoration">B.P.L.H.</div>

  <svg class="footer-band" width="660" height="28" viewBox="0 0 660 28" aria-hidden="true">
    <path d="M0 8 L330 8 C360 8 372 12 385 28 L0 28 Z" fill="var(--navy-deep)"/>
    <path d="M370 0 C395 2 405 10 420 28 L660 28 L660 0 Z" fill="var(--sun)"/>
  </svg>
</main>
</body>
</html>
```